BrightCampusPicks blogger needs pagely book cover

The title for the book is "Mapping School Options: A Handbook for Reading Campus Pages to Spend Little on a Stronger Degree"

Title must legible for Pagely store. I only need to front, no back or spine. The cover should be optimized to display on Vornex. Image size should be 1880x2500.

This book isn’t about how to apply to college or which classes to take or how to score higher on the QRT. It’s only focus is on how to use college websites to create a better college list. This is part of my general approach for families to use information important to their situation to find affordable colleges. I've attached a file with some covers from the category I like. I'm pretty flexible regarding colors, fonts, etc.

Target Market(s)

Parents of high school students worried about paying for college.

Industry/Entity Type

College

Requirements
Must have
• Title must be legible at small size.

```html
<!DOCTYPE html>
<html lang="en">
<head>
<meta charset="utf-8">
<title>Mapping School Options – Book Cover</title>
<link rel="stylesheet" href="https://fonts.googleapis.com/css2?family=Barlow+Condensed:wght@500;600&family=Open+Sans:ital,wght@1,400&display=swap">
<style>
  :root {
    --brand-blue: #1789ee;
    --ink: #0d0d0d;
    --paper-light: #ffffff;
    --paper-edge: #dcdcdc;
    --band-text: #ffffff;
    --art-dark: #3a3a3a;
    --art-green: #b9c4a8;
  }
  html, body {
    margin: 0;
    padding: 0;
    width: 902px;
    height: 1200px;
    overflow: hidden;
  }
  .cover {
    position: relative;
    width: 902px;
    height: 1200px;
    background: radial-gradient(ellipse at 50% 55%, var(--paper-light) 35%, var(--paper-edge) 100%);
    overflow: hidden;
  }
  .cover-title {
    position: absolute;
    left: 0;
    top: 0;
    width: 902px;
    height: 420px;
  }
  .title-line {
    font-family: "Barlow Condensed", "Arial Narrow", sans-serif;
    font-weight: 600;
  }
  .title-line--primary { fill: var(--brand-blue); }
  .title-line--secondary { fill: var(--ink); }
  .cover-art {
    position: absolute;
    left: 270px;
    top: 470px;
    width: 360px;
    height: 360px;
    border-radius: 50%;
    background: radial-gradient(circle at 50% 35%, var(--art-dark) 0 22%, rgba(255,255,255,0) 40%),
                radial-gradient(circle at 50% 78%, var(--art-green) 0 20%, rgba(255,255,255,0) 38%);
    opacity: 0.85;
  }
  .cover-subtitle {
    position: absolute;
    left: 0;
    top: 838px;
    width: 902px;
    margin: 0;
    text-align: center;
    font-family: "Open Sans", "Helvetica", sans-serif;
    font-style: italic;
    font-weight: 400;
    font-size: 36px;
    line-height: 50px;
    color: var(--ink);
  }
  .author-band {
    position: absolute;
    left: 0;
    top: 1040px;
    width: 902px;
    height: 160px;
    background: var(--brand-blue);
    display: flex;
    align-items: center;
    justify-content: center;
  }
  .author-name {
    margin: 0;
    font-family: "Barlow Condensed", "Arial Narrow", sans-serif;
    font-weight: 600;
    font-size: 88px;
    letter-spacing: 2px;
    color: var(--band-text);
  }
</style>
</head>
<body>
  <main class="cover">
    <svg class="cover-title" viewBox="0 0 902 420" aria-label="Mapping School Options">
      <text class="title-line title-line--primary" x="451" y="252" text-anchor="middle" font-size="314" textLength="770" lengthAdjust="spacingAndGlyphs">MAPPING</text>
      <text class="title-line title-line--secondary" x="451" y="403" text-anchor="middle" font-size="172" textLength="760" lengthAdjust="spacingAndGlyphs">SCHOOL OPTIONS</text>
    </svg>

    <div class="cover-art" role="img" aria-label="Illustration of a black graduation cap floating above stacks of banknotes"></div>

    <p class="cover-subtitle">A Handbook for Reading Campus Pages<br>to Spend Little on a Stronger Degree</p>

    <footer class="author-band">
      <p class="author-name">DANA WHITFIELD</p>
    </footer>
  </main>
</body>
</html>
```